OLVAK Web Design (Need help to re-design our website)

We need someone to help us re-design our website and launch it. All contents for the website are ready. (https://olvak.example.au/)

-Rearrange categories:
1. Heating & Cooling
2. Remove Home Appliance
3. Remove Entertainment

Home page - redesign (It will be a nice touch if the banner is in the loop).

NOTE:
-Brand colour blue and orange.
-Try using professional fonts (Example: Helvetica, etc.)
-The website's Footer should be readable and use light colour.

Target Market(s)

Residentials & commercial buildings

Industry/Entity Type

Heat Ventilation and Cooling Industry, Technology , Renewables

Coding

Coded - Design and coding required

Colors
0094D4
00A9DD
6FCCEA
C7EBF8
E9F6FB
59FF00
82FF00
B8FF75
E3FFCB
F4FFEA
F0912C
F2A743
F7CA91
FBE8D2
FDF5EE

Requirements
Nice to have
• Effects/transition on the words/copy/images.

```html
<!DOCTYPE html>
<html lang="en">
<head>
<meta charset="utf-8">
<title>OLVAK — Heating &amp; Cooling</title>
<link href="https://fonts.googleapis.com/css2?family=Arimo:wght@400;600;700&family=Bebas+Neue&display=swap" rel="stylesheet">
<style>
:root{
  --blue:#1a61b0;
  --blue-dark:#15539a;
  --orange:#f5921f;
  --orange-soft:#f39a2b;
  --ink:#111;
  --grey-bg:#f3f3f3;
  --strip:#f1f1f1;
  --white:#fff;
}
*{box-sizing:border-box;margin:0;padding:0}
html,body{width:1200px;height:3364px;overflow:hidden}
body{font-family:"Arimo",Helvetica,Arial,sans-serif;color:var(--ink);background:var(--white);position:relative}
.abs{position:absolute}
.btn{position:absolute;display:flex;align-items:center;justify-content:center;font-size:13px;color:var(--white);border-radius:14px 4px 14px 4px}
.btn-orange{background:var(--orange)}
.btn-blue{background:var(--blue)}
.btn-white{background:var(--white);color:var(--ink)}

/* top bar */
.topbar{left:0;top:0;width:1200px;height:35px;background:var(--blue);color:var(--white);font-size:12.5px}
.topbar .promo{left:141px;top:10px}
.topbar .item{top:9px;display:flex;align-items:center;gap:8px}

/* nav */
.brand{font-weight:700;color:var(--blue);letter-spacing:5px;display:flex;align-items:center;gap:12px}
.brand .dot{width:30px;height:30px;border-radius:50%;background:var(--orange)}
.nav-brand{left:141px;top:55px;font-size:34px}
.menu{top:66px;font-size:13px}
.menu.active{color:var(--blue);font-weight:600}
.search{left:1023px;top:56px;width:36px;height:35px;background:var(--blue);border-radius:10px 3px 10px 3px;display:flex;align-items:center;justify-content:center}

/* hero */
.hero{left:0;top:114px;width:1200px;height:543px;background:linear-gradient(100deg,#6f6a55 0%,#a39b88 30%,#d6d2cb 55%,#cfc8be 75%,#9c8f7f 100%)}
.hero-text{left:141px;top:312px;color:var(--white)}
.hero-kicker{font-size:19px;font-weight:700}
.hero-title{font-family:"Bebas Neue",Impact,sans-serif;font-size:76px;line-height:68px;margin-top:2px;letter-spacing:0.5px}
.hero-sub{font-size:19px;font-weight:700;margin-top:0}

/* headings */
.h2{font-size:26px;font-weight:700;letter-spacing:0.3px}
.h2 span{color:var(--blue)}
.center{left:0;width:1200px;text-align:center}

/* about */
.frame-big{left:133px;top:752px;width:365px;height:353px;background:var(--white);border-radius:70px 70px 4px 70px;box-shadow:0 6px 24px rgba(0,0,0,.12)}
.photo-big{left:156px;top:775px;width:319px;height:307px;border-radius:56px 56px 0 4px;background:linear-gradient(180deg,#dfe6ea 0%,#b7936f 35%,#a57e5c 70%,#b9bcbc 100%)}
.frame-small{left:408px;top:986px;width:182px;height:175px;background:var(--white);border-radius:40px 40px 40px 40px;box-shadow:0 6px 20px rgba(0,0,0,.14)}
.photo-small{left:424px;top:1000px;width:149px;height:146px;border-radius:32px 32px 32px 4px;background:linear-gradient(180deg,#e7eef2 0%,#cfd6da 60%,#5d8a3a 100%)}
.about-text{left:651px;top:858px;width:410px}
.about-text p{font-size:13.5px;line-height:24.3px;margin-top:16px}

/* offering */
.offering-band{left:0;top:1254px;width:1200px;height:209px;background:var(--grey-bg)}
.panel{top:1463px;width:600px;height:388px;color:var(--white);text-align:center}
.panel-res{left:0;background:linear-gradient(180deg,#2865ab,#1d5aa3)}
.panel-com{left:600px;background:linear-gradient(180deg,#f5a03a,#f08f25)}
.panel svg{position:absolute;left:273px;top:142px}
.panel h3{position:absolute;left:0;width:600px;top:212px;font-size:27px;font-weight:700;letter-spacing:.5px}
.panel p{position:absolute;left:70px;width:460px;top:252px;font-size:13.5px;line-height:20px}
.panel .btn{left:261px;top:305px;width:77px;height:35px}

/* reviews */
.review{top:2043px;width:283px;text-align:center;font-size:13px;line-height:23px}
.review .quote{padding:0 14px}
.review-side .quote{margin-top:60px}
.strip{position:absolute;left:0;width:283px;height:58px;background:var(--strip);border-radius:4px}
.avatar{position:absolute;width:62px;height:62px;border-radius:50%;border:4px solid var(--white);box-shadow:0 2px 6px rgba(0,0,0,.2);background:linear-gradient(135deg,#d9b89b,#a67c5e)}
.who{position:absolute;text-align:left;line-height:16px}
.who b{font-size:14px;font-weight:700;display:block}
.who small{font-size:11px}
.stars{position:absolute;font-size:11px;letter-spacing:2px;color:var(--orange)}
.review-main{left:459px;height:229px;background:var(--blue);color:var(--white);border-radius:8px;box-shadow:0 8px 20px rgba(0,0,0,.18);overflow:visible}
.review-main .quote{margin-top:14px;padding:0 14px}
.review-main .strip{top:169px;height:60px;background:var(--orange);border-radius:0 0 8px 8px}
.arrow{width:34px;height:34px;border-radius:50%;background:var(--white);box-shadow:0 2px 8px rgba(0,0,0,.15);display:flex;align-items:center;justify-content:center}

/* compliant */
.compliant-band{left:0;top:2398px;width:1200px;height:551px;background:var(--grey-bg)}
.badge{top:2625px;width:140px;height:140px;border-radius:50%}
.save{left:247px;top:2851px;width:706px;height:176px;background:var(--orange);border-radius:90px 0 90px 0;color:var(--white)}
.save-line{position:absolute;left:0;width:706px;top:18px;display:flex;justify-content:center;align-items:center;gap:12px;font-weight:700}
.save-line .small{font-size:25px}
.save-line .big{font-size:74px;letter-spacing:1px}

/* footer */
.foot-brand{left:141px;top:3097px;font-size:33px}
.foot-rule{left:141px;top:3160px;width:177px;height:1px;background:#ddd}
.social{top:3176px;width:31px;height:31px;border-radius:50%;border:1.5px solid var(--orange)}
.foot-h{top:3102px;font-size:15px;font-weight:700;letter-spacing:.3px}
.links{left:403px;top:3134px;list-style:none;font-size:12.5px;line-height:22px}
.contact{left:595px;font-size:12.5px;line-height:19px}
.contact .txt{position:absolute;left:42px;top:0;white-space:nowrap}
.news-text{left:837px;top:3134px;font-size:12.5px;line-height:19px}
.news-input{left:837px;top:3180px;width:222px;height:34px;border:1px solid #bbb;border-radius:3px;font-size:11.5px;color:#666;padding:10px 8px}
.subscribe{left:837px;top:3225px;width:140px;height:35px;background:var(--orange);color:var(--white);font-weight:700;font-size:15px;display:flex;align-items:center;justify-content:center;border-radius:2px;letter-spacing:.5px}
.bottombar{left:0;top:3312px;width:1200px;height:52px;background:var(--blue);color:var(--white);font-size:12.5px}
</style>
</head>
<body>

<!-- Top bar -->
<div class="abs topbar">
  <div class="abs promo">Don't miss our: Latest Promotions</div>
  <div class="abs item" style="left:801px">
    <svg width="18" height="18" viewBox="0 0 24 24" fill="none" stroke="#fff" stroke-width="2"><path d="M5 3h4l2 5-3 2a12 12 0 0 0 6 6l2-3 5 2v4a2 2 0 0 1-2 2A18 18 0 0 1 3 5a2 2 0 0 1 2-2z"/></svg>
    <span>1800 555 014</span>
  </div>
  <div class="abs item" style="left:920px">
    <svg width="20" height="14" viewBox="0 0 20 14" fill="none" stroke="#fff" stroke-width="1.6"><rect x="1" y="1" width="18" height="12"/><path d="M1 1l9 7 9-7"/></svg>
    <span>info@olvak.example.au</span>
  </div>
</div>

<!-- Navigation -->
<div class="abs brand nav-brand"><span class="dot"></span>OLVAK</div>
<div class="abs menu active" style="left:481px">Home</div>
<div class="abs menu" style="left:550px">Heating &amp; Cooling</div>
<div class="abs menu" style="left:687px">Our Story</div>
<div class="abs menu" style="left:776px">Contact Us</div>
<div class="btn btn-orange" style="left:872px;top:56px;width:141px;height:35px">Book Appointment</div>
<div class="abs search">
  <svg width="14" height="14" viewBox="0 0 14 14" fill="none" stroke="#fff" stroke-width="2"><circle cx="6" cy="6" r="4.2"/><path d="M9.2 9.2L13 13"/></svg>
</div>

<!-- Hero -->
<div class="abs hero" role="img" aria-label="Family relaxing on a sofa beneath a wall-mounted air conditioner, with a palm plant in the foreground"></div>
<div class="abs hero-text">
  <div class="hero-kicker">REVOLUTIONISE</div>
  <div class="hero-title">HEATING &amp; COOLING</div>
  <div class="hero-sub">INDUSTRY AUSTRALIA WIDE</div>
</div>
<div class="btn btn-orange" style="left:141px;top:430px;width:78px;height:33px">Explore</div>
<div class="btn btn-blue" style="left:229px;top:430px;width:141px;height:33px">Book Appointment</div>

<!-- About -->
<div class="abs frame-big"></div>
<div class="abs photo-big" role="img" aria-label="Heat pump water heater installed against a brick wall"></div>
<div class="abs frame-small"></div>
<div class="abs photo-small" role="img" aria-label="Outdoor heat pump unit on grass"></div>
<div class="abs about-text">
  <div class="h2">ABOUT <span>OLVAK</span></div>
  <p>OLVAK is a company dedicated to manufacturing and installing energy-efficient products that reduce energy consumption, save costs, and promote sustainability. Our mission is to help individuals and businesses reduce their carbon footprint while also enhancing their comfort and quality of life.</p>
</div>
<div class="btn btn-orange" style="left:651px;top:1048px;width:91px;height:35px">Read More</div>

<!-- Offering -->
<div class="abs offering-band"></div>
<div class="abs center h2" style="top:1385px">OFFERING <span>SOLUTIONS FOR</span></div>
<div class="abs center" style="top:1424px;font-size:14px">Please select from a category below that best suits your requirements.</div>

<div class="abs panel panel-res" role="img" aria-label="Residential home with outdoor air conditioning units, tinted blue">
  <svg width="54" height="54" viewBox="0 0 54 54" fill="none" stroke="#fff" stroke-width="2"><path d="M4 24L27 6l23 18"/><path d="M10 20v30h34V20"/><rect x="21" y="16" width="12" height="8"/><rect x="14" y="30" width="8" height="8"/><rect x="32" y="30" width="8" height="8"/><path d="M24 50V38h6v12"/></svg>
  <h3>RESIDENTIALS</h3>
  <p>Lorem ipsum dolor sit amet, consectetuer adipiscing elit, sed diam nonummy nibh euismod tincidunt ut laoreet dolore magna aliquam erat volutpat.</p>
  <div class="btn btn-white">Explore</div>
</div>
<div class="abs panel panel-com" role="img" aria-label="Commercial office building at sunset, tinted orange">
  <svg width="54" height="54" viewBox="0 0 54 54" fill="none" stroke="#fff" stroke-width="2"><rect x="16" y="6" width="22" height="44"/><rect x="4" y="24" width="12" height="26"/><rect x="38" y="18" width="12" height="32"/><path d="M21 12h4M29 12h4M21 20h4M29 20h4M21 28h4M29 28h4M21 36h4M29 36h4M24 50v-8h6v8M8 30h4M8 38h4M42 24h4M42 32h4M42 40h4"/></svg>
  <h3>COMMERCIAL</h3>
  <p>Lorem ipsum dolor sit amet, consectetuer adipiscing elit, sed diam nonummy nibh euismod tincidunt ut laoreet dolore magna aliquam erat volutpat.</p>
  <div class="btn btn-white">Explore</div>
</div>

<!-- Reviews -->
<div class="abs center h2" style="top:1985px">CLIENT <span>REVIEWS</span></div>

<div class="abs arrow" style="left:91px;top:2138px">
  <svg width="16" height="10" viewBox="0 0 16 10" fill="none" stroke="#aaa" stroke-width="1.4"><path d="M15 5H1M5 1L1 5l4 4"/></svg>
</div>
<div class="abs arrow" style="left:1075px;top:2138px">
  <svg width="16" height="10" viewBox="0 0 16 10" fill="none" stroke="#1a61b0" stroke-width="1.4"><path d="M1 5h14M11 1l4 4-4 4"/></svg>
</div>

<div class="abs review review-side" style="left:142px">
  <div class="quote">Lorem ipsum dolor sit amet, consectetuer adipiscing elit, sed diam nonu mmy nibh euismod tincidunt ut laoreet dolore magna aliquam erat volut pat. Ut wisi enim ad minim veniam, quis nostrud exerci.</div>
  <div class="strip" style="top:205px"></div>
  <div class="avatar" style="left:15px;top:184px" role="img" aria-label="Customer portrait"></div>
  <div class="who" style="left:94px;top:224px"><b>Jordan K.</b><small>Lorem ipsum</small></div>
  <div class="stars" style="left:203px;top:230px">★★★★★</div>
</div>

<div class="abs review review-main">
  <div class="quote">Lorem ipsum dolor sit amet, consectetuer adipiscing elit, sed diam nonu mmy nibh euismod tincidunt ut laoreet dolore magna aliquam erat volut pat. Ut wisi enim ad minim veniam, quis nostrud exerci.</div>
  <div class="strip"></div>
  <div class="avatar" style="left:14px;top:148px;background:linear-gradient(135deg,#c9a48a,#7d5a45)" role="img" aria-label="Customer portrait"></div>
  <div class="who" style="left:94px;top:188px;color:#fff"><b>Ellen Marsh</b><small>Lorem ipsum</small></div>
  <div class="stars" style="left:203px;top:193px;color:#fff">★★★★★</div>
</div>

<div class="abs review review-side" style="left:777px">
  <div class="quote">Lorem ipsum dolor sit amet, consectetuer adipiscing elit, sed diam nonu mmy nibh euismod tincidunt ut laoreet dolore magna aliquam erat volut pat. Ut wisi enim ad minim veniam, quis nostrud exerci.</div>
  <div class="strip" style="top:205px"></div>
  <div class="avatar" style="left:15px;top:184px;background:linear-gradient(135deg,#e0c2a3,#b48a64)" role="img" aria-label="Customer portrait"></div>
  <div class="who" style="left:94px;top:224px"><b>Nadia Ruiz</b><small>Lorem ipsum</small></div>
  <div class="stars" style="left:203px;top:230px">★★★★★</div>
</div>

<!-- Compliance -->
<div class="abs compliant-band"></div>
<div class="abs center h2" style="top:2540px;line-height:32px">FULLY COMPLIANT WITH<br><span>ALL GOVERNMENT REBATES</span></div>
<div class="abs badge" style="left:350px;background:radial-gradient(circle,#1f6b3a 0 38%,#d9b64a 40% 100%)" role="img" aria-label="Quality certification badge"></div>
<div class="abs badge" style="left:520px;background:radial-gradient(circle,#c8d6ea 0 40%,#1d3f86 42% 100%)" role="img" aria-label="Australian owned and operated badge"></div>
<div class="abs badge" style="left:708px;background:radial-gradient(circle,#ffffff 0 55%,#e3e5e8 57% 100%)" role="img" aria-label="Energy saving badge"></div>

<div class="abs save">
  <div class="save-line"><span class="small">SAVE UPTO</span><span class="big">75%</span><span class="small">ELECTRICITY COST</span></div>
  <div class="btn btn-blue" style="left:282px;top:102px;width:142px;height:33px">Contact Us Today</div>
</div>

<!-- Footer -->
<div class="abs brand foot-brand"><span class="dot"></span>OLVAK</div>
<div class="abs foot-rule"></div>
<div class="abs social" style="left:141px"></div>
<div class="abs social" style="left:189px"></div>
<div class="abs social" style="left:237px"></div>
<div class="abs social" style="left:286px"></div>

<div class="abs foot-h" style="left:403px">QUICK LINKS</div>
<ul class="abs links">
  <li>Home</li><li>Heating &amp; Cooling</li><li>Our Story</li><li>Support</li><li>Latest Promotions</li><li>Contact Us</li>
</ul>

<div class="abs foot-h" style="left:595px">CONTACT DETAILS</div>
<div class="abs contact" style="top:3134px">
  <svg width="32" height="30" viewBox="0 0 32 30" fill="none" stroke="#333" stroke-width="1.3"><rect x="8" y="4" width="14" height="25"/><rect x="2" y="14" width="6" height="15"/><path d="M12 9h2M16 9h2M12 14h2M16 14h2M12 19h2M16 19h2M13 29v-5h4v5"/><circle cx="26" cy="17" r="4"/><path d="M26 21v8"/></svg>
  <div class="txt">48 Harbour Rd,<br>Lakeview VIC 3999</div>
</div>
<div class="abs contact" style="top:3180px">
  <svg width="32" height="30" viewBox="0 0 24 24" fill="none" stroke="#333" stroke-width="1.2"><path d="M5 3h4l2 5-3 2a12 12 0 0 0 6 6l2-3 5 2v4a2 2 0 0 1-2 2A18 18 0 0 1 3 5a2 2 0 0 1 2-2z"/></svg>
  <div class="txt">PHONE<br>1800 555 014</div>
</div>
<div class="abs contact" style="top:3228px">
  <svg width="32" height="30" viewBox="0 0 32 30" fill="none" stroke="#333" stroke-width="1.3"><path d="M2 12l14-10 14 10v16H2z"/><path d="M2 12l14 10 14-10"/><path d="M9 9h14"/></svg>
  <div class="txt">EMAIL<br>info@olvak.example.au</div>
</div>

<div class="abs foot-h" style="left:837px">NEWSLETTER SIGN UP</div>
<div class="abs news-text">Enter your email address to register<br>to our newsletter subscription</div>
<div class="abs news-input">Enter your email address</div>
<div class="abs subscribe">SUBSCRIBE</div>

<div class="abs bottombar">
  <div class="abs" style="left:141px;top:19px">© 2024 OLVAK. All Rights Reserved.</div>
  <div class="abs" style="right:141px;top:19px">Privacy Policy &nbsp; I &nbsp; Terms &amp; Conditions &nbsp; I &nbsp; Sitemap</div>
</div>

</body>
</html>
```